Casa Vantora
Stationery / Business Cards
Professional
Ramiro Quesada
Engineering
427 Brisadores
Suite 392
Laredo, TX
USA
1-800 597-RNQZ
ramiro@casavantora.com.mx
www.casavantora.com.mx
Logo & Website on background
"Control de Iluminacion
Audio y Video Distribuido
Home Theater
Telefonia, Voz y Datos
Integracion de Sistemas
Circuito Cerrado de TV
Ingenieria y Diseno"

```html
<!DOCTYPE html>
<html lang="es">
<head>
<meta charset="utf-8">
<title>Casa Vantora — Stationery</title>
<link href="https://fonts.googleapis.com/css2?family=Open+Sans:wght@400;600;700&display=swap" rel="stylesheet">
<style>
:root{
  --bg:#6e3f22;
  --blue:#1f6db5;
  --blue-light:#4fa3e0;
  --navy:#0f2c4c;
  --black:#16181b;
  --paper:#ffffff;
  --grey:#8c9096;
  --grey-light:#d9dcdf;
  --ink:#3a3f45;
}
*{margin:0;padding:0;box-sizing:border-box}
html,body{width:1200px;height:307px;overflow:hidden;background:var(--bg);font-family:"Open Sans",Arial,sans-serif}
.canvas{position:relative;width:1200px;height:307px}
.piece{position:absolute;overflow:hidden;box-shadow:0 2px 5px rgba(0,0,0,.35)}
.brand{display:flex;align-items:center;gap:3px;color:var(--blue);font-weight:700;white-space:nowrap}
.brand .dot{display:inline-block;border-radius:50%;background:var(--blue)}
.brand.light{color:#fff}
.brand.light .dot{background:#fff}
.swoosh{position:absolute;left:0;width:100%}
.small{font-size:4px;line-height:6px;color:var(--ink)}
.small.light{color:#dfe8f2}

/* business cards */
.card{width:112px;height:68px}
.card.front{background:var(--paper)}
.card.navy{background:var(--navy)}
.card.black{background:var(--black)}
.card .brand{position:absolute;left:8px;top:10px;font-size:8px}
.card .brand .dot{width:9px;height:9px}
.card .contact{position:absolute;left:8px;top:28px}
.card .services{position:absolute;right:6px;top:8px;text-align:right}
.card .center{position:absolute;left:0;right:0;top:22px;display:flex;justify-content:center}
.card .center .brand{position:static;font-size:9px}

/* letterhead */
.letterhead{left:288px;top:19px;width:120px;height:264px;background:var(--paper)}
.letterhead .brand{position:absolute;left:10px;top:12px;font-size:8px}
.letterhead .brand .dot{width:9px;height:9px}
.letterhead .contact{position:absolute;right:8px;top:10px;text-align:right}
.faint-circle{position:absolute;border-radius:50%;background:var(--blue);opacity:.08}
.letterhead .foot{position:absolute;left:8px;bottom:6px;color:#fff;font-size:4px}

/* envelopes */
.env-back{left:414px;top:19px;width:304px;height:112px;background:var(--paper)}
.env-card{left:420px;top:112px;width:160px;height:100px;background:var(--paper)}
.env-front{left:416px;top:148px;width:304px;height:132px;background:var(--paper)}
.env-front .brand{position:absolute;left:12px;top:54px;font-size:8px}
.env-front .brand .dot{width:9px;height:9px}
.env-front .address{position:absolute;left:12px;top:72px}
.env-front .to{position:absolute;left:150px;top:80px}

/* folder */
.folder-cover{left:730px;top:19px;width:246px;height:264px;background:linear-gradient(135deg,#2a82cc,#134e8c)}
.folder-cover .site{position:absolute;left:0;right:0;bottom:58px;text-align:center;color:#cfe4f6;font-size:5px}
.folder-inner{left:976px;top:19px;width:150px;height:264px;background:var(--paper)}
.folder-inner .brand{position:absolute;left:12px;top:14px;font-size:9px}
.folder-inner .brand .dot{width:10px;height:10px}
.folder-inner .pocket{position:absolute;left:0;right:0;bottom:0;height:112px;background:#f3f5f7;border-top:1px solid var(--grey-light)}

/* notepads */
.note{width:64px;background:var(--paper)}
.note .brand{position:absolute;left:6px;top:8px;font-size:6px}
.note .brand .dot{width:6px;height:6px}
</style>
</head>
<body>
<div class="canvas">

  <!-- business cards -->
  <section class="piece card front" style="left:8px;top:28px">
    <div class="brand"><span class="dot"></span>Casa Vantora</div>
    <div class="small contact">Ramiro Quesada<br>Engineering<br>1-800 597-RNQZ<br>ramiro@casavantora.com.mx</div>
    <svg class="swoosh" style="bottom:0" height="12" viewBox="0 0 112 12" preserveAspectRatio="none"><path d="M0 12 L0 6 Q56 -2 112 8 L112 12Z" fill="var(--blue)"/></svg>
  </section>
  <section class="piece card navy" style="left:124px;top:28px">
    <div class="center"><div class="brand light"><span class="dot"></span>Casa Vantora</div></div>
    <div class="small light" style="position:absolute;left:0;right:0;bottom:8px;text-align:center">www.casavantora.com.mx</div>
  </section>
  <section class="piece card front" style="left:8px;top:110px">
    <div class="small contact" style="top:8px">427 Brisadores<br>Suite 392<br>Laredo, TX USA</div>
    <div class="small services">Control de Iluminacion<br>Audio y Video Distribuido<br>Home Theater<br>Telefonia, Voz y Datos<br>Integracion de Sistemas<br>Circuito Cerrado de TV<br>Ingenieria y Diseno</div>
    <svg class="swoosh" style="bottom:0" height="10" viewBox="0 0 112 10" preserveAspectRatio="none"><path d="M0 10 L0 4 Q56 -2 112 6 L112 10Z" fill="var(--blue)"/></svg>
  </section>
  <section class="piece card navy" style="left:124px;top:110px">
    <div class="small light contact" style="top:8px">Ramiro Quesada<br>Engineering<br>1-800 597-RNQZ<br>ramiro@casavantora.com.mx</div>
    <div class="small light services" style="top:34px">Home Theater<br>Ingenieria y Diseno</div>
  </section>
  <section class="piece card black" style="left:8px;top:194px">
    <div class="center"><div class="brand light"><span class="dot"></span>Casa Vantora</div></div>
    <div class="small light" style="position:absolute;left:0;right:0;bottom:8px;text-align:center">www.casavantora.com.mx</div>
  </section>
  <section class="piece card black" style="left:124px;top:194px">
    <div class="small light contact" style="top:8px">Ramiro Quesada<br>Engineering<br>1-800 597-RNQZ<br>ramiro@casavantora.com.mx</div>
    <div class="small light services" style="top:40px">Laredo, TX<br>USA</div>
  </section>

  <!-- letterhead -->
  <section class="piece letterhead">
    <div class="brand"><span class="dot"></span>Casa Vantora</div>
    <div class="small contact" style="top:32px">427 Brisadores<br>Suite 392<br>Laredo, TX USA<br>1-800 597-RNQZ</div>
    <div class="faint-circle" style="left:20px;top:90px;width:80px;height:80px"></div>
    <svg class="swoosh" style="bottom:0" height="26" viewBox="0 0 120 26" preserveAspectRatio="none"><path d="M0 26 L0 12 Q60 -4 120 10 L120 26Z" fill="var(--blue)"/></svg>
    <div class="foot">www.casavantora.com.mx</div>
  </section>

  <!-- envelopes -->
  <section class="piece env-back">
    <svg class="swoosh" style="top:0" height="70" viewBox="0 0 304 70" preserveAspectRatio="none"><path d="M0 0 L304 0 L304 8 L152 70 L0 8Z" fill="var(--grey)"/><circle cx="152" cy="40" r="12" fill="#fff" opacity=".9"/></svg>
  </section>
  <section class="piece env-card">
    <div class="faint-circle" style="left:50px;top:18px;width:60px;height:60px;opacity:.12"></div>
  </section>
  <section class="piece env-front">
    <svg class="swoosh" style="top:0" height="48" viewBox="0 0 304 48" preserveAspectRatio="none"><path d="M0 0 L304 0 L304 22 Q150 -6 0 44Z" fill="var(--blue)"/><path d="M0 44 Q150 -6 304 22 L304 26 Q150 2 0 48Z" fill="var(--blue-light)"/></svg>
    <div class="brand"><span class="dot"></span>Casa Vantora</div>
    <div class="small address">427 Brisadores, Suite 392<br>Laredo, TX USA</div>
    <div class="small to">www.casavantora.com.mx</div>
  </section>

  <!-- folder -->
  <section class="piece folder-cover">
    <div class="faint-circle" style="left:63px;top:72px;width:120px;height:120px;background:#fff;opacity:.12"></div>
    <div class="site">www.casavantora.com.mx</div>
    <svg class="swoosh" style="bottom:0" height="44" viewBox="0 0 246 44" preserveAspectRatio="none"><path d="M0 44 L0 26 Q123 -8 246 20 L246 44Z" fill="#0f3d70"/></svg>
  </section>
  <section class="piece folder-inner">
    <div class="brand"><span class="dot"></span>Casa Vantora</div>
    <div class="small" style="position:absolute;left:12px;top:34px">Control de Iluminacion<br>Audio y Video Distribuido<br>Home Theater</div>
    <div class="pocket"></div>
    <svg class="swoosh" style="bottom:0" height="24" viewBox="0 0 150 24" preserveAspectRatio="none"><path d="M0 24 L0 12 Q75 -4 150 10 L150 24Z" fill="var(--blue)"/></svg>
  </section>

  <!-- notepads -->
  <section class="piece note" style="left:1130px;top:48px;height:130px">
    <div class="brand"><span class="dot"></span>Casa Vantora</div>
    <svg class="swoosh" style="bottom:0" height="14" viewBox="0 0 64 14" preserveAspectRatio="none"><path d="M0 14 L0 6 Q32 -2 64 6 L64 14Z" fill="var(--blue)"/></svg>
  </section>
  <section class="piece note" style="left:1130px;top:196px;height:86px">
    <svg class="swoosh" style="bottom:0" height="14" viewBox="0 0 64 14" preserveAspectRatio="none"><path d="M0 14 L0 6 Q32 -2 64 6 L64 14Z" fill="var(--blue)"/></svg>
  </section>

</div>
</body>
</html>
```